Mietwagen Brandel

We need a web(graphic) design for an landing page on our internet portal providing a search engine to select a rental car. The search engine is using more as 150 rental car providers to find the best price. A comprehensive filter make the selection very quick and effective.
The design should be modern and clean. E.g. this website is what we have seen looks in our opinion good: http://cars.drivolumbo.com

Reason: The decision takes a bit longer

Please change size to 960 px by 1500 px. Also please provide how many photoshop layers your design includes. Thank you.

```html
<!DOCTYPE html>
<html lang="en">
<head>
<meta charset="utf-8">
<title>Car Rental Portal</title>
<link href="https://fonts.googleapis.com/css2?family=Lato:wght@400;700;900&display=swap" rel="stylesheet">
<style>
:root{
  --accent:#7bbfe0;
  --ink:#222629;
  --text:#333;
  --muted:#8a8a8a;
  --line:#d8d8d8;
  --band:#eef5f9;
  --white:#fff;
}
*{box-sizing:border-box;margin:0;padding:0}
html,body{width:960px;height:1200px;overflow:hidden;background:var(--white)}
body{position:relative;font-family:'Lato',sans-serif;color:var(--text)}
.abs{position:absolute}

/* header */
.site-header{position:absolute;left:0;top:0;width:960px;height:70px;background:var(--white);box-shadow:0 2px 3px rgba(0,0,0,.22);z-index:2}
.brand{position:absolute;left:99px;top:15px;font-size:28px;font-weight:700;color:#111;letter-spacing:-.3px}
.main-nav a{position:absolute;top:27px;font-family:Arial,Helvetica,sans-serif;font-size:14.5px;color:#111;text-decoration:none}
.main-nav .active{left:401px;top:0;width:81px;height:70px;background:var(--accent);color:var(--white);text-align:center;line-height:70px}
.main-nav .active::after{content:"";position:absolute;left:35px;bottom:-6px;border:6px solid transparent;border-top-color:var(--accent);border-bottom:0}

/* search form */
.form-title{left:100px;top:115px;font-size:20px;font-weight:700;color:var(--ink)}
.field-label{font-size:12px;font-weight:700;color:#111}
.field{height:34px;border:1px solid #dcdcdc;background:var(--white);font-size:11.5px;color:var(--muted);padding:0 12px;line-height:32px}
.field svg{position:absolute;right:10px;top:10px}
.btn{background:var(--accent);color:var(--white);font-size:13px;font-weight:700;display:flex;align-items:center;justify-content:center;gap:10px}

/* hero */
.hero-title{left:475px;top:108px;font-size:50px;font-weight:900;color:var(--ink);letter-spacing:-.5px}
.hero-sub{left:476px;top:160px;font-size:24px;color:var(--ink)}
.hero-copy{left:476px;top:201px;width:382px;font-size:12px;line-height:18px;color:#222}
.hero-visual{left:420px;top:288px;width:460px;height:256px;background:radial-gradient(ellipse at 60% 45%,#f4f4f4 0%,#e4e6e8 45%,rgba(255,255,255,0) 72%)}
.slider-dots{left:760px;top:562px}

/* feature band */
.feature-band{position:absolute;left:0;top:630px;width:960px;height:281px;background:var(--band);border-top:1px solid #c9d0d4;border-bottom:1px solid #c9d0d4}
.feature h2{font-size:27px;font-weight:700;color:var(--ink);letter-spacing:-.3px;line-height:1}
.feature h3{font-size:17px;font-weight:700;color:#555;margin-top:5px}
.feature p{margin-top:13px;font-size:12px;line-height:22px;color:#444;text-align:justify;letter-spacing:.1px}
.divider{left:479px;top:42px;height:218px;border-left:1px dashed var(--accent)}

/* gallery */
.gallery-title{left:99px;top:933px;font-size:27px;font-weight:700;color:var(--ink)}
.thumb{top:978px;width:178px;height:104px}

/* footer */
.footer-line{left:99px;top:1111px;width:760px;border-top:1px solid #c6c6c6}
.legal{left:99px;top:1147px;font-size:12px;color:#999}
.social{right:98px;top:1147px;font-size:12px;color:#222;text-align:right}
</style>
</head>
<body>

<header class="site-header">
  <div class="brand">Company Logo</div>
  <nav class="main-nav">
    <a class="active" href="#">HOME</a>
    <a href="#" style="left:493px">MY BOOKING</a>
    <a href="#" style="left:614px">HELP</a>
    <a href="#" style="left:680px">ABOUT US</a>
    <a href="#" style="left:782px">CONTACT</a>
  </nav>
</header>

<!-- search form -->
<h1 class="abs form-title">Where and when..?</h1>

<div class="abs field-label" style="left:101px;top:149px">Country:</div>
<div class="abs field" style="left:100px;top:166px;width:330px">Australia
  <svg width="12" height="12" viewBox="0 0 12 12"><path d="M2 4l4 4 4-4" fill="none" stroke="#222" stroke-width="2"/></svg></div>

<div class="abs field-label" style="left:101px;top:214px">Pick-up Location :</div>
<div class="abs field" style="left:100px;top:231px;width:330px">Type pickup City or Airport code</div>

<div class="abs field-label" style="left:101px;top:279px">Pickup Date and Time:</div>
<div class="abs field" style="left:100px;top:296px;width:330px">1/1/2014
  <svg width="15" height="15" viewBox="0 0 15 15"><rect x="1" y="2" width="13" height="12" fill="none" stroke="#444"/><rect x="1" y="2" width="13" height="3" fill="#444"/><path d="M4 0v3M11 0v3M1 8h13M1 11h13M4.5 5v9M7.5 5v9M10.5 5v9" stroke="#444"/></svg></div>

<div class="abs field-label" style="left:101px;top:344px">Return Date and Time:</div>
<div class="abs field" style="left:100px;top:361px;width:330px">1/1/2014
  <svg width="15" height="15" viewBox="0 0 15 15"><rect x="1" y="2" width="13" height="12" fill="none" stroke="#444"/><rect x="1" y="2" width="13" height="3" fill="#444"/><path d="M4 0v3M11 0v3M1 8h13M1 11h13M4.5 5v9M7.5 5v9M10.5 5v9" stroke="#444"/></svg></div>

<div class="abs field-label" style="left:101px;top:409px">I live in:</div>
<div class="abs field" style="left:100px;top:426px;width:330px">Australia</div>

<div class="abs hero-visual" role="img" aria-label="White compact SUV photographed on a soft grey studio floor"></div>

<div class="abs field-label" style="left:100px;top:474px">Driver Age:</div>
<div class="abs field" style="left:100px;top:491px;width:154px">25+
  <svg width="12" height="12" viewBox="0 0 12 12"><path d="M2 4l4 4 4-4" fill="none" stroke="#222" stroke-width="2"/></svg></div>

<div class="abs field-label" style="left:276px;top:474px">Return to same Location:</div>
<div class="abs field" style="left:276px;top:491px;width:154px">Yes
  <svg width="12" height="12" viewBox="0 0 12 12"><path d="M2 4l4 4 4-4" fill="none" stroke="#222" stroke-width="2"/></svg></div>

<div class="abs btn" style="left:310px;top:550px;width:120px;height:44px">Search
  <svg width="13" height="13" viewBox="0 0 14 14"><circle cx="7" cy="7" r="7" fill="#fff"/><path d="M4 7h5M7 4.5L9.5 7 7 9.5" fill="none" stroke="#7bbfe0" stroke-width="2"/></svg></div>

<!-- hero -->
<div class="abs hero-title">Welcome</div>
<div class="abs hero-sub">The Number 1 Car Rental Portal</div>
<p class="abs hero-copy">it's a Slider hear we can write our specialitys and about us and etc. Here we can write our specialitys and about us and etc. Here we can write our specialitys and about us and etc. Here we can write our specialitys and about us and etc.</p>
<svg class="abs slider-dots" width="80" height="12" viewBox="0 0 80 12">
  <g fill="#fff" stroke="#7bbfe0" stroke-width="2.5">
    <circle cx="7" cy="6" r="4.5"/><circle cx="23" cy="6" r="4.5"/><circle cx="39" cy="6" r="4.5"/><circle cx="56" cy="6" r="4.5"/><circle cx="73" cy="6" r="4.5"/>
  </g>
</svg>

<!-- features -->
<section class="feature-band">
  <div class="abs divider"></div>
  <div class="abs feature" style="left:123px;top:42px;width:328px">
    <h2>Rent a Car</h2>
    <h3>We Deserve the Cheapest Rate</h3>
    <p>Donec sit amet eros. Lorem ipsum dolor sit amet consect-etuer adipiscing elit. Mauris fermentum dictum magna. Sed let aliquam leo. Ut tell. us dolor dapibus eget elementum vel cursus eleifend elit.</p>
  </div>
  <div class="abs btn" style="left:330px;top:210px;width:120px;height:44px">Read More
    <svg width="13" height="13" viewBox="0 0 14 14"><circle cx="7" cy="7" r="7" fill="#fff"/><path d="M4 7h5M7 4.5L9.5 7 7 9.5" fill="none" stroke="#7bbfe0" stroke-width="2"/></svg></div>

  <div class="abs feature" style="left:507px;top:42px;width:328px">
    <h2>Customer Service</h2>
    <h3>24/7 Help line and Best Services</h3>
    <p>Nulla dui. Fusce feugiat malesuada odio. Morbi nunc odio gravida atcursus nec uctus a lorem. Maecenas tristique orci ac sem. Duis ultricies pharetra magna. Donec accumsan malesuada orci.</p>
  </div>
  <div class="abs btn" style="left:715px;top:210px;width:120px;height:44px">Read More
    <svg width="13" height="13" viewBox="0 0 14 14"><circle cx="7" cy="7" r="7" fill="#fff"/><path d="M4 7h5M7 4.5L9.5 7 7 9.5" fill="none" stroke="#7bbfe0" stroke-width="2"/></svg></div>
</section>

<!-- gallery -->
<h2 class="abs gallery-title">Gallery</h2>
<svg class="abs" style="left:802px;top:941px" width="40" height="16" viewBox="0 0 40 16">
  <path d="M9 2L3 8l6 6M31 2l6 6-6 6" fill="none" stroke="#222" stroke-width="2.5"/>
</svg>
<div class="abs thumb" style="left:100px;background:linear-gradient(135deg,#5d6a55,#8a7a68 50%,#3f4a3a)" role="img" aria-label="Bronze sedan driving past city buildings"></div>
<div class="abs thumb" style="left:294px;background:linear-gradient(180deg,#9a9ea3,#d8d9da 55%,#6d7176)" role="img" aria-label="White hatchback on a road under a cloudy sky"></div>
<div class="abs thumb" style="left:487px;background:radial-gradient(ellipse at 50% 55%,#3a3c3f 0%,#e2e3e4 70%)" role="img" aria-label="Black SUV on a light grey backdrop"></div>
<div class="abs thumb" style="left:681px;background:radial-gradient(ellipse at 50% 55%,#8a8c8e 0%,#eeeeee 70%)" role="img" aria-label="Silver SUV on a pale backdrop"></div>

<!-- footer -->
<div class="abs footer-line"></div>
<div class="abs legal">company name© 2014privacy policy</div>
<div class="abs social">Follow us: Chatterly, Linkpost, Blog</div>

</body>
</html>
```